Industrial Pop Up Display For Tradeshow Booth

Our company manufactures private label cleaning products and needs to have a pop up display for our tradeshow booth. We make cleaning products for the automotive, household, marine, shoe, sports, pet, and technology markets. We would like the display to have our logo and communicate that we manufacture for those markets. Imagery of bottles and manufacturing processes are encouraged.

```html
<!DOCTYPE html>
<html lang="en">
<head>
<meta charset="utf-8">
<title>Norvale Products – Tradeshow Pop Up Display</title>
<link href="https://fonts.googleapis.com/css2?family=Oswald:wght@400;600&family=Lato:wght@700&display=swap" rel="stylesheet">
<style>
  :root {
    --orange: #f7981f;
    --black: #030303;
    --white: #ffffff;
    --paper: #f8f9fa;
    --band: #f2f3f5;
    --ink-gray: #6a6a6c;
    --facet: #d9d6d6;
  }
  * { margin: 0; padding: 0; box-sizing: border-box; }
  html, body { width: 1200px; height: 1200px; overflow: hidden; background: var(--paper); }
  .display {
    position: relative; width: 1200px; height: 1200px; overflow: hidden;
    background: var(--paper);
  }
  .facet-backdrop {
    position: absolute; left: 0; top: 0; width: 1200px; height: 520px;
    background: linear-gradient(180deg, var(--facet) 0%, #ebe9e9 35%, var(--paper) 100%);
  }
  .footer-band {
    position: absolute; left: 0; top: 1125px; width: 1200px; height: 75px;
    background: var(--band);
  }
  .brand-banner { position: absolute; left: 428px; top: 0; width: 343px; height: 422px; }
  .brand-name {
    position: absolute; left: 428px; top: 140px; width: 343px;
    text-align: center; color: var(--white);
    font-family: 'Oswald', sans-serif; font-weight: 600;
    font-size: 80px; line-height: 88px; letter-spacing: -1px;
  }
  .brand-tagline {
    position: absolute; left: 428px; top: 318px; width: 343px;
    text-align: center; color: var(--white);
    font-family: 'Oswald', sans-serif; font-weight: 400;
    font-size: 27px; letter-spacing: 1px;
  }
  .tile {
    position: absolute; width: 142px; height: 142px;
    box-shadow: 6px 8px 12px rgba(0,0,0,0.28);
  }
  .tile--orange { background: var(--orange); }
  .tile--black { background: var(--black); }
  .photo { position: absolute; box-shadow: 6px 8px 12px rgba(0,0,0,0.28); }
  .photo--auto { background: linear-gradient(120deg, #7f858c 0%, #c9a36a 55%, #e8d9b8 100%); }
  .photo--tech { background: linear-gradient(120deg, #f1f1f1 0%, #2a2c30 45%, #5fb9d8 70%, #e9d6c4 100%); }
  .photo--marine { background: linear-gradient(160deg, #3d5a66 0%, #7f9aa3 45%, #f2f2f2 75%, #ffffff 100%); }
  .photo--home { background: linear-gradient(160deg, #ffffff 0%, #b9bcbf 50%, #7b7f83 100%); }
  .photo--shoe { background: linear-gradient(100deg, #ffffff 0%, #7a4a30 35%, #2b1d17 60%, #8a5a3c 85%, #ffffff 100%); }
  .contact {
    position: absolute; left: 0; top: 1030px; width: 1200px;
    text-align: center; color: var(--ink-gray);
    font-family: 'Lato', sans-serif; font-weight: 700;
    font-size: 40px; line-height: 48px;
  }
  .contact-frame { position: absolute; left: 290px; top: 1046px; width: 620px; height: 74px; }
</style>
</head>
<body>
<main class="display">
  <div class="facet-backdrop" role="img" aria-label="Faint grey faceted geometric background pattern"></div>
  <div class="footer-band"></div>

  <svg class="brand-banner" viewBox="0 0 343 422" aria-hidden="true">
    <polygon points="0,0 343,0 343,367 171.5,422 0,367" fill="var(--orange)"/>
  </svg>
  <div class="brand-name">NORVALE<br>PRODUCTS</div>
  <div class="brand-tagline">BLEND PACK DELIVER</div>

  <div class="tile tile--orange" style="left:32px;top:370px"></div>
  <div class="tile tile--black" style="left:316px;top:512px"></div>
  <div class="tile tile--orange" style="left:742px;top:512px"></div>
  <div class="tile tile--black" style="left:32px;top:654px"></div>
  <div class="tile tile--orange" style="left:174px;top:654px"></div>
  <div class="tile tile--black" style="left:600px;top:654px"></div>
  <div class="tile tile--orange" style="left:1026px;top:654px"></div>
  <div class="tile tile--orange" style="left:742px;top:796px"></div>

  <div class="photo photo--auto" style="left:32px;top:512px;width:284px;height:142px" role="img" aria-label="Man polishing a car headlight with a yellow cloth"></div>
  <div class="photo photo--tech" style="left:458px;top:512px;width:284px;height:142px" role="img" aria-label="Gloved hand wiping a computer monitor with a spray bottle nearby"></div>
  <div class="photo photo--marine" style="left:316px;top:654px;width:284px;height:142px" role="img" aria-label="Crew members scrubbing the deck of a white boat"></div>
  <div class="photo photo--marine" style="left:316px;top:796px;width:142px;height:142px" aria-hidden="true"></div>
  <div class="photo photo--home" style="left:884px;top:370px;width:142px;height:284px" role="img" aria-label="Household appliances: fridge, washer, microwave, television and vacuum"></div>
  <div class="photo photo--home" style="left:1026px;top:512px;width:142px;height:142px" aria-hidden="true"></div>
  <div class="photo photo--shoe" style="left:742px;top:654px;width:284px;height:142px" role="img" aria-label="Row of polished brown and black leather dress shoes"></div>

  <svg class="contact-frame" viewBox="0 0 620 74" aria-hidden="true">
    <path d="M146,7 H26 Q7,7 7,26 V48 Q7,67 26,67 H60" fill="none" stroke="var(--orange)" stroke-width="5"/>
    <path d="M474,7 H594 Q613,7 613,26 V48 Q613,67 594,67 H562" fill="none" stroke="var(--orange)" stroke-width="5"/>
  </svg>
  <div class="contact">
    <div class="contact-phone">888.555.0142</div>
    <div class="contact-email">info@norvaleproducts.com</div>
  </div>
</main>
</body>
</html>
```